Family owned plumbing contractor needs eye catching business card design

Business cards that are unique, eye catching, and provide customers with general company information, such as name, address, phone number, website, employee name/title, cell phone #, & email address. We are transitioning to a new logo that utilizes a more retro feel, so we are interested in seeing some cool old school designs in the mix. We are liking the dark background on some of the samples on this website. If that is workable with our artwork, we would like to see that incorporated into the design.
Contact Information for Business Card
Copperline Pipeworks, Inc.
www.copperlinepipeworks.example
(555) 630-2918 phone
Nevada License #64205
California License #5870413
Glen Harwick, President
(555) 418-9063 cell
glen@copperlinepipeworks.example
Residential * Commercial * Service
Requirements
Must have
- The business card details listed above & logo provided.
Nice to have
- I made some notes about color options in the description.

```html
<!DOCTYPE html>
<html lang="en">
<head>
<meta charset="utf-8">
<title>Copperline Pipeworks, Inc. – Business Card</title>
<link rel="stylesheet" href="https://fonts.googleapis.com/css2?family=Josefin+Sans:wght@600;700&display=swap">
<style>
  :root {
    --backdrop: #7d8082;
    --card-black: #0c0c0d;
    --card-marble: #1a1a1c;
    --ink-white: #f2f2f0;
    --teal: #4fbfae;
    --teal-dark: #3a9e90;
    --faint: rgba(255,255,255,0.07);
  }
  * { box-sizing: border-box; margin: 0; padding: 0; }
  html, body { width: 1200px; height: 800px; overflow: hidden; }
  body {
    background: var(--backdrop);
    font-family: "Josefin Sans", "Futura", sans-serif;
    position: relative;
  }
  .card {
    position: absolute;
    left: 337px;
    width: 526px;
    height: 300px;
    background: var(--card-black);
    color: var(--ink-white);
    overflow: hidden;
    box-shadow: 0 6px 18px rgba(0,0,0,0.35);
  }
  .card--back { top: 70px; padding: 22px 28px; }
  .card--front { top: 420px; }

  /* Back side */
  .back__company {
    font-size: 25px; font-weight: 700; letter-spacing: 1.5px;
    text-transform: uppercase; text-align: center;
  }
  .back__watermark {
    position: absolute; left: 0; right: 0; top: 118px;
    text-align: center; font-size: 44px; font-weight: 700;
    color: var(--faint); white-space: nowrap;
  }
  .back__person { text-align: center; margin-top: 14px; position: relative; }
  .back__name { font-size: 22px; font-weight: 700; letter-spacing: 1.5px; text-transform: uppercase; }
  .back__title { font-size: 11px; font-weight: 700; letter-spacing: 1px; text-transform: uppercase; margin-top: 1px; }
  .contact-list { list-style: none; margin-top: 16px; position: relative; }
  .contact-list li {
    display: flex; align-items: center; gap: 8px;
    font-size: 14.5px; font-weight: 700; letter-spacing: 1px;
    text-transform: uppercase; height: 33px;
  }
  .contact-icon { width: 26px; height: 26px; flex: none; }
  .licenses { margin-top: 10px; position: relative; color: var(--teal); }
  .licenses p { font-size: 13px; font-weight: 700; letter-spacing: 1px; text-transform: uppercase; line-height: 17px; }

  /* Front side */
  .front__texture {
    position: absolute; inset: 0;
    background: radial-gradient(ellipse at 30% 40%, var(--card-marble), var(--card-black) 70%);
  }
  .front__services {
    position: absolute; top: 24px; left: 0; right: 0; text-align: center;
    font-size: 19px; font-weight: 700; letter-spacing: 1.5px; text-transform: uppercase;
  }
  .front__mark {
    position: absolute; top: 92px; left: 0; right: 0;
    display: flex; align-items: center; justify-content: center; gap: 14px;
  }
  .front__mark-dot { width: 22px; height: 22px; border-radius: 50%; background: var(--teal); }
  .front__name {
    font-size: 34px; font-weight: 700; color: var(--teal); letter-spacing: 1px;
  }
  .front__ribbon { position: absolute; left: 93px; top: 214px; width: 340px; height: 40px; }
  .front__url {
    position: absolute; left: 93px; top: 214px; width: 340px; height: 40px;
    display: flex; align-items: center; justify-content: center;
    font-size: 12.5px; font-weight: 700; color: var(--card-black);
    letter-spacing: 0.5px; text-transform: uppercase;
  }
</style>
</head>
<body>

<section class="card card--back" aria-label="Business card, contact side">
  <div class="back__watermark" aria-hidden="true">Copperline Pipeworks</div>
  <h1 class="back__company" style="position:relative">Copperline Pipeworks, Inc.</h1>
  <div class="back__person">
    <p class="back__name">Glen Harwick</p>
    <p class="back__title">President</p>
  </div>
  <ul class="contact-list">
    <li>
      <svg class="contact-icon" viewBox="0 0 26 26" aria-hidden="true">
        <circle cx="13" cy="13" r="11.5" fill="none" stroke="var(--teal)" stroke-width="1.6"/>
        <path d="M7 11c0-2 3-3 6-3s6 1 6 3l-2 1-1-2h-6l-1 2z" fill="var(--teal)"/>
        <rect x="8.5" y="13" width="9" height="5" rx="1" fill="var(--teal)"/>
      </svg>
      (555) 630-2918 Phone
    </li>
    <li>
      <svg class="contact-icon" viewBox="0 0 26 26" aria-hidden="true">
        <circle cx="13" cy="13" r="11.5" fill="none" stroke="var(--teal)" stroke-width="1.6"/>
        <rect x="9.5" y="6.5" width="7" height="13" rx="1.5" fill="none" stroke="var(--ink-white)" stroke-width="1.4"/>
      </svg>
      (555) 418-9063 Cell
    </li>
    <li>
      <svg class="contact-icon" viewBox="0 0 26 26" aria-hidden="true">
        <circle cx="13" cy="13" r="11.5" fill="none" stroke="var(--teal)" stroke-width="1.6"/>
        <text x="13" y="17.5" text-anchor="middle" font-size="13" font-weight="700" fill="var(--ink-white)" font-family="Josefin Sans, sans-serif">@</text>
      </svg>
      glen@copperlinepipeworks.example
    </li>
  </ul>
  <div class="licenses">
    <p>Nevada License #64205</p>
    <p>California License #5870413</p>
  </div>
</section>

<section class="card card--front" aria-label="Business card, logo side">
  <div class="front__texture" role="img" aria-label="Black cracked marble texture background"></div>
  <p class="front__services">Residential * Commercial * Service</p>
  <div class="front__mark">
    <span class="front__mark-dot" aria-hidden="true"></span>
    <span class="front__name">Copperline Pipeworks, Inc.</span>
  </div>
  <svg class="front__ribbon" viewBox="0 0 340 40" aria-hidden="true">
    <polygon points="0,8 22,8 22,36 0,36 10,22" fill="var(--teal-dark)"/>
    <polygon points="340,8 318,8 318,36 340,36 330,22" fill="var(--teal-dark)"/>
    <rect x="16" y="4" width="308" height="28" fill="var(--teal)"/>
  </svg>
  <p class="front__url">www.copperlinepipeworks.example</p>
</section>

</body>
</html>
```